Bref créative
Business card for an optometrist
Professional
Dr. Toren "Bax" Holmqvist
Optometric Physician
418 Marlow Lane, 2nd Floor, Fernbrook, NJ 07135
Visioncare.Fernbrook@quilmail.com
www.fernbrookvisioncare.com
NJ Lic. #4817
We would like to have Fernbrook Visioncare logo as the first line followed by the doctor's name and license number. Then either in the center or at the bottom right/left, we would like the address, phone & fax number and email/website.
M_____________________________
HAS AN APPOINTMENT ON
and then show boxes for each day of the wk (excluding sunday) and then:
DATE_______AT____________(AM/PM)
IF UNABLE TO KEEP APPOINTMENT, KINDLY GIVE 24 HOURS NOTICE

```html
<!DOCTYPE html>
<html lang="en">
<head>
<meta charset="utf-8">
<title>Fernbrook Visioncare — Stationery</title>
<link rel="stylesheet" href="https://fonts.googleapis.com/css2?family=Cinzel:wght@500&family=Open+Sans:wght@400;600&display=swap">
<style>
  :root {
    --blue: #1f7fc3;
    --blue-light: #63b3e3;
    --orange: #e8772e;
    --paper: #ffffff;
    --stage: #ffffff;
    --ink: #4a4f55;
    --edge: #e3e6ea;
  }
  * { margin: 0; padding: 0; box-sizing: border-box; }
  html, body { width: 1200px; height: 936px; overflow: hidden; }
  body { background: var(--stage); position: relative; font-family: "Open Sans", Arial, sans-serif; color: var(--ink); }

  .sheet { position: absolute; background: var(--paper); border: 1px solid var(--edge); overflow: hidden; }
  .sheet svg.wave { position: absolute; display: block; }

  .brand { position: absolute; display: flex; align-items: center; gap: 8px; }
  .brand-dot { border-radius: 50%; background: var(--orange); flex: none; }
  .brand-name { font-family: "Cinzel", Georgia, serif; font-weight: 500; color: var(--blue); line-height: 1.05; letter-spacing: 0.04em; }

  /* Letterhead */
  .letterhead { left: 190px; top: 68px; width: 381px; height: 546px; }
  .letterhead .brand { left: 22px; top: 30px; }
  .letterhead .brand-dot { width: 14px; height: 14px; }
  .letterhead .brand-name { font-size: 11px; }
  .contact-list { position: absolute; left: 236px; top: 22px; list-style: none; font-size: 5.6px; line-height: 9px; color: var(--ink); }
  .contact-list li { display: flex; align-items: center; gap: 4px; }
  .contact-list li::before { content: ""; width: 5px; height: 5px; border-radius: 50%; background: var(--blue); flex: none; }
  .watermark-circle { position: absolute; left: 125px; top: 190px; width: 130px; height: 130px; border-radius: 50%; background: var(--orange); opacity: 0.12; }
  .letterhead .wave { left: 0; bottom: 0; width: 381px; height: 70px; }

  /* Folder */
  .folder { left: 634px; top: 36px; width: 538px; height: 578px; }
  .folder .wave { left: 0; top: 0; width: 90px; height: 578px; }
  .folder .brand { left: 190px; top: 220px; gap: 14px; }
  .folder .brand-dot { width: 40px; height: 40px; }
  .folder .brand-name { font-size: 34px; }

  /* Business card front */
  .card-front { left: 38px; top: 655px; width: 195px; height: 81px; }
  .card-front .brand { left: 10px; top: 8px; gap: 5px; }
  .card-front .brand-dot { width: 9px; height: 9px; }
  .card-front .brand-name { font-size: 8px; }
  .card-front .wave { right: 0; top: 0; width: 80px; height: 81px; }
  .card-details { position: absolute; left: 10px; top: 32px; width: 118px; }
  .doctor-name { font-size: 5.6px; font-weight: 600; color: var(--blue); line-height: 1.2; }
  .doctor-title { font-size: 4.2px; line-height: 1.3; margin-bottom: 3px; }
  .card-contact { list-style: none; font-size: 4px; line-height: 5.2px; }
  .card-contact li { white-space: nowrap; }

  /* Appointment card */
  .card-back { left: 38px; top: 748px; width: 195px; height: 97px; padding: 9px 12px; font-size: 5px; line-height: 1; color: var(--ink); }
  .appt-line { display: flex; align-items: flex-end; gap: 2px; margin-bottom: 5px; }
  .appt-line .rule { flex: 1; border-bottom: 0.6px solid var(--ink); height: 5px; }
  .appt-label { margin-bottom: 6px; font-weight: 600; letter-spacing: 0.04em; }
  .day-boxes { display: flex; gap: 6px; margin-bottom: 8px; }
  .day-boxes span { display: flex; align-items: center; gap: 2px; }
  .day-boxes span::after { content: ""; width: 7px; height: 7px; border: 0.6px solid var(--ink); }
  .appt-note { font-size: 4.2px; letter-spacing: 0.02em; }

  /* Envelopes */
  .envelope-front { left: 266px; top: 667px; width: 452px; height: 216px; }
  .envelope-front .brand { left: 16px; top: 26px; gap: 6px; }
  .envelope-front .brand-dot { width: 11px; height: 11px; }
  .envelope-front .brand-name { font-size: 10px; }
  .envelope-front .wave { right: 0; top: 0; width: 140px; height: 216px; }

  .envelope-back { left: 741px; top: 665px; width: 431px; height: 218px; }
  .envelope-back .wave { left: 0; top: 0; width: 431px; height: 80px; }
  .envelope-back .web { position: absolute; left: 0; right: 0; top: 20px; text-align: center; font-family: "Cinzel", Georgia, serif; font-size: 7px; letter-spacing: 0.2em; color: #ffffff; }
</style>
</head>
<body>

  <section class="sheet letterhead" aria-label="Letterhead">
    <div class="brand">
      <span class="brand-dot"></span>
      <span class="brand-name">Fernbrook<br>Visioncare</span>
    </div>
    <ul class="contact-list">
      <li>418 Marlow Lane, 2nd Floor</li>
      <li>Fernbrook, NJ 07135</li>
      <li>Tel (201) 555-0148</li>
      <li>Fax (201) 555-0149</li>
      <li>Visioncare.Fernbrook@quilmail.com</li>
    </ul>
    <div class="watermark-circle"></div>
    <svg class="wave" viewBox="0 0 381 70" preserveAspectRatio="none">
      <path d="M0 44 C110 70 240 44 381 18" fill="none" stroke="var(--orange)" stroke-width="1.4"/>
      <path d="M0 52 C120 72 250 52 381 24 L381 70 L0 70 Z" fill="var(--blue)"/>
      <path d="M0 58 C130 74 260 60 381 36 L381 70 L0 70 Z" fill="var(--blue-light)" opacity="0.5"/>
    </svg>
  </section>

  <section class="sheet folder" aria-label="Presentation folder">
    <svg class="wave" viewBox="0 0 90 578" preserveAspectRatio="none">
      <path d="M0 0 L44 0 C10 120 70 250 40 330 C16 400 50 480 30 578 L0 578 Z" fill="var(--blue)"/>
      <path d="M44 0 C10 120 70 250 40 330 C16 400 50 480 30 578" fill="none" stroke="var(--blue-light)" stroke-width="6" opacity="0.6"/>
      <path d="M52 0 C18 120 78 250 48 330 C24 400 58 480 38 578" fill="none" stroke="var(--orange)" stroke-width="1.2"/>
    </svg>
    <div class="brand">
      <span class="brand-dot"></span>
      <span class="brand-name">Fernbrook<br>Visioncare</span>
    </div>
  </section>

  <section class="sheet card-front" aria-label="Business card front">
    <div class="brand">
      <span class="brand-dot"></span>
      <span class="brand-name">Fernbrook<br>Visioncare</span>
    </div>
    <div class="card-details">
      <p class="doctor-name">Dr. Toren "Bax" Holmqvist</p>
      <p class="doctor-title">Optometric Physician · NJ Lic. #4817</p>
      <ul class="card-contact">
        <li>418 Marlow Lane, 2nd Floor, Fernbrook, NJ 07135</li>
        <li>Tel (201) 555-0148 · Fax (201) 555-0149</li>
        <li>Visioncare.Fernbrook@quilmail.com</li>
        <li>www.fernbrookvisioncare.com</li>
      </ul>
    </div>
    <svg class="wave" viewBox="0 0 80 81" preserveAspectRatio="none">
      <path d="M40 0 C20 28 60 50 50 81 L80 81 L80 0 Z" fill="var(--blue)"/>
      <path d="M34 0 C14 28 54 50 44 81" fill="none" stroke="var(--orange)" stroke-width="0.8"/>
    </svg>
  </section>

  <section class="sheet card-back" aria-label="Appointment card">
    <div class="appt-line">M<span class="rule"></span></div>
    <div class="appt-label">HAS AN APPOINTMENT ON</div>
    <div class="day-boxes">
      <span>MON</span><span>TUE</span><span>WED</span><span>THU</span><span>FRI</span><span>SAT</span>
    </div>
    <div class="appt-line">DATE<span class="rule"></span>AT<span class="rule"></span>(AM/PM)</div>
    <div class="appt-note">IF UNABLE TO KEEP APPOINTMENT, KINDLY GIVE 24 HOURS NOTICE</div>
  </section>

  <section class="sheet envelope-front" aria-label="Envelope front">
    <div class="brand">
      <span class="brand-dot"></span>
      <span class="brand-name">Fernbrook<br>Visioncare</span>
    </div>
    <svg class="wave" viewBox="0 0 140 216" preserveAspectRatio="none">
      <path d="M140 40 C110 110 40 150 0 216 L140 216 Z" fill="var(--blue)"/>
      <path d="M140 28 C104 104 36 146 -6 216" fill="none" stroke="var(--orange)" stroke-width="1"/>
    </svg>
  </section>

  <section class="sheet envelope-back" aria-label="Envelope back">
    <svg class="wave" viewBox="0 0 431 80" preserveAspectRatio="none">
      <path d="M0 0 L431 0 L431 52 C300 62 140 74 0 54 Z" fill="var(--blue)"/>
      <path d="M0 60 C140 80 300 68 431 58" fill="none" stroke="var(--blue-light)" stroke-width="3"/>
    </svg>
    <div class="web">www.fernbrookvisioncare.com</div>
  </section>

</body>
</html>
```